Window Treatment business needs website redesigned.

We need a revamp and refresh of our current site www.velmorin.ca
Looking to attract very high end customer. It should be a very simple design with very little text. This site will be visited by prospective homeowners, designers, builders and architects. They should feel that they are dealing with a high-end product selection, where experience, customer service and unique product offering is the focus. The content will be to highlight our services and highlight the manufacturers we sell, using a few rich photos to highlight the products. We should NOT look like we are a very large company. It should NOT have discounts/savings buttons and many menus to choose from. We offer over 15 years experience to narrow the many market options, to provide the right technical solution.
We specialize in products that are not readily available on the market and specifically motorized systems for indoors and outdoors.
Our main suppliers are Quarnel.com, Dexavo.com
We carry our own locally manufactured product line of roller shades.
Main product pictures should be of roller shades, outdoor bug screens, awnings and outdoor pergolas.

Reason: I understand that Christmas is coming up real short and many people are extremely busy. If you have a CREATIVE gifting you still want to submit, I look forward to your idea!

Reason: Due to holiday season, we have not had sufficient time to review to make a final decision. Thank you for your patience!

Target Market(s)

High end home owners, designers, builders, architects

Industry/Entity Type

Contractor

Coding

Coded - Design and coding required

Number of Pages Required

3 page

Font styles to use
Sans Serif

Requirements
Must have
• Landing page with full size image like homepage of borvela.it
• Products page that highlights products with simple product shot image, description and link to manufacturer.
• On main page a scrolling of customer reviews.
• I want a very simple, eye-catching, emotional image for homepage. It does not need to include any product image.
• An image that shows technology combining/meshing with hand craftsmanship.
• Focus is on design.
• http://www.borvela.it/en/gallery is a great layout and design.
Nice to have
• Logo shape for icons and watermark should be used.
• Look like and have simple motion effects like tirquel.com or manvexo.com
Should not have
• Generic/standard looking feel like gostrel.com or plinkwardcove.ca
• No use of green as background only subtle text.
• Lots of text and pages.

```html
<!DOCTYPE html>
<html lang="en">
<head>
<meta charset="utf-8">
<title>Velmorin — Window Treatment Solutions</title>
<link rel="stylesheet" href="https://fonts.googleapis.com/css2?family=Ubuntu:wght@300;400;500&family=Raleway:wght@400;500&display=swap">
<style>
:root{
  --green:#6cbf3c;
  --ink:#222;
  --muted:#7a7a7a;
  --field:#e6e6e6;
  --soft-bg:#f1f1f1;
  --footer-line:#4a4f57;
  --orange:#e8552b;
  --quote-orange:#f0a03a;
  --social-blue:#3b78c2;
  --white:#fff;
}
*{box-sizing:border-box;margin:0;padding:0}
html,body{width:1200px;height:2659px;overflow:hidden;background:var(--white)}
body{font-family:"Ubuntu",sans-serif;color:var(--ink);position:relative}
a{color:inherit;text-decoration:none}

/* Header */
.site-header{position:absolute;left:0;top:0;width:1200px;height:106px}
.brand{position:absolute;left:80px;top:18px;display:flex;align-items:center;gap:10px}
.brand-mark{width:62px;height:62px;border-radius:50%;border:5px solid var(--ink);background:var(--white)}
.brand-name{font-size:34px;font-weight:400;color:var(--green);line-height:1}
.brand-tag{font-size:12px;color:var(--muted);margin-top:3px}
.contact-bar{position:absolute;left:822px;top:0;width:298px;height:36px;background:#efefef;display:flex;align-items:center;justify-content:flex-end;gap:8px;padding-right:12px;clip-path:polygon(6% 0,100% 0,100% 100%,0 100%)}
.contact-bar .phone{display:flex;align-items:center;gap:8px;font-size:15px;margin-right:12px}
.social-dot{width:26px;height:26px;border-radius:50%;border:2px solid var(--social-blue)}
.main-nav{position:absolute;right:80px;top:61px;display:flex;gap:25px;font-size:14px}
.main-nav a{padding-bottom:6px}
.main-nav a.active{color:var(--green);border-bottom:2px solid var(--green)}

/* Hero */
.hero{position:absolute;left:0;top:105px;width:1200px;height:570px;overflow:hidden}
.hero-photo{position:absolute;inset:0;background:
  radial-gradient(ellipse 230px 160px at 800px 90px,rgba(140,110,85,.9),rgba(140,110,85,0)),
  radial-gradient(ellipse 260px 260px at 1000px 220px,rgba(95,125,160,.95),rgba(95,125,160,0)),
  radial-gradient(ellipse 110px 90px at 870px 230px,rgba(225,185,40,.85),rgba(225,185,40,0)),
  radial-gradient(ellipse 460px 130px at 800px 540px,rgba(215,190,155,.95),rgba(215,190,155,0)),
  radial-gradient(ellipse 420px 300px at 560px 420px,rgba(70,60,50,.8),rgba(70,60,50,0)),
  linear-gradient(90deg,#0c0c0c 0%,#1a1a1a 30%,#2e2b27 50%,#5d5248 68%,#7f7468 85%,#8d8c8a 100%)}
.hero-copy{position:absolute;left:80px;top:124px;color:var(--white)}
.hero-kicker{font-size:31px;font-weight:300;color:var(--green)}
.hero-title{font-size:48px;font-weight:400;line-height:1.02;margin-top:6px}
.hero-title span{display:block;color:var(--green)}
.hero-lead{width:470px;font-size:14px;line-height:21px;margin-top:12px;font-family:"Raleway",sans-serif}
.btn-outline{display:inline-block;border:1.5px solid var(--green);color:var(--green);font-size:13px;font-weight:500;letter-spacing:.5px;text-transform:uppercase;text-align:center}
.hero .btn-outline{margin-top:30px;width:142px;height:34px;line-height:31px;color:#9fd47d}

/* Section titles */
.section-title{font-size:36px;font-weight:400;color:var(--ink)}
.section-title em{font-style:normal;color:var(--green)}

/* About */
.about{position:absolute;left:80px;top:718px;width:665px}
.about .section-title{display:flex;align-items:center;gap:10px}
.about .icon-ring{width:42px;height:42px;border-radius:50%;border:4px solid var(--ink)}
.about-lead{font-size:18px;line-height:26px;color:#4a5060;margin-top:22px}
.about-note{font-size:16px;line-height:22px;color:var(--green);margin-top:20px}
.about-body{font-size:13.5px;line-height:21px;color:var(--ink);margin-top:20px;font-family:"Raleway",sans-serif}

/* Estimate form */
.estimate{position:absolute;left:852px;top:718px;width:330px}
.estimate .section-title{margin-bottom:18px}
.field{display:block;width:330px;height:43px;background:var(--field);margin-bottom:10px;font-size:13px;color:#777;padding:12px 14px;font-family:"Raleway",sans-serif}
.field.tall{height:80px}
.estimate .btn-outline{margin-top:6px;width:141px;height:34px;line-height:31px;background:var(--white)}

/* Products */
.products{position:absolute;left:0;top:1182px;width:1200px;height:486px;background:linear-gradient(160deg,#ededed,#f6f6f6 50%,#eeeeee)}
.products .section-title{position:absolute;left:80px;top:54px}
.product-card{position:absolute;top:126px;width:241px}
.product-photo{width:241px;height:179px}
.product-name{font-size:18px;font-weight:400;margin-top:24px;color:var(--ink);font-family:"Raleway",sans-serif}
.product-desc{font-size:12.5px;line-height:21px;color:var(--muted);margin-top:10px;font-family:"Raleway",sans-serif}
.arrow{position:absolute;width:22px;height:40px}

/* Reviews */
.reviews .section-title{position:absolute;left:80px;top:1728px}
.review{position:absolute;top:1820px;display:flex}
.avatar{position:relative;width:124px;height:124px;border-radius:50%;border:5px solid var(--orange);background:
  radial-gradient(circle at 50% 38%,#e2c2a8 0,#c99c7c 32%,rgba(0,0,0,0) 52%),
  linear-gradient(180deg,#b08a6c,#7a5640)}
.avatar::after{content:"";position:absolute;right:-22px;top:30px;border-left:20px solid var(--orange);border-top:9px solid transparent;border-bottom:9px solid transparent}
.review-body{margin-left:28px;margin-top:20px;width:320px}
.review-quote{font-size:15px;line-height:23px;color:var(--ink)}
.qmark{color:var(--quote-orange);font-size:34px;font-family:Georgia,serif;line-height:0;vertical-align:-10px}
.review-name{font-size:15px;color:var(--quote-orange);margin-top:14px;padding-left:30px;text-transform:uppercase}

/* Partners */
.partners .section-title{position:absolute;left:80px;top:2083px}
.partner{position:absolute;top:2147px;width:241px;height:92px;border:1px solid #d8d8d8;display:flex;align-items:center;justify-content:center}

/* Footer */
.site-footer{position:absolute;left:0;top:2317px;width:1200px;height:289px;background:
  radial-gradient(ellipse 400px 160px at 300px 260px,rgba(70,80,95,.55),rgba(70,80,95,0)),
  radial-gradient(ellipse 300px 140px at 980px 60px,rgba(60,70,85,.5),rgba(60,70,85,0)),
  linear-gradient(180deg,#1a1e24,#252a31);color:#e4e4e4}
.footer-col{position:absolute;top:50px}
.footer-col h3{font-size:20px;font-weight:400;color:var(--green);padding-bottom:8px;border-bottom:1px solid var(--footer-line)}
.footer-col ul{list-style:none;margin-top:14px;font-size:13px;font-family:"Raleway",sans-serif}
.quick li{line-height:21px;padding-left:12px;position:relative}
.quick li::before{content:"";position:absolute;left:0;top:8px;border-left:4px solid #ddd;border-top:3px solid transparent;border-bottom:3px solid transparent}
.contact li{display:flex;gap:10px;line-height:18px;margin-bottom:10px}
.contact .call{color:var(--green);font-size:17px}
.newsletter p{font-size:13px;line-height:18px;margin-top:14px;font-family:"Raleway",sans-serif}
.newsletter .input{width:200px;height:27px;background:var(--white);margin-top:14px;color:#999;font-size:11px;padding:6px 8px}
.newsletter .subscribe{display:inline-block;margin-top:12px;background:var(--green);color:var(--white);font-size:12px;padding:4px 10px}
.follow li{display:flex;align-items:center;gap:12px;line-height:26px;margin-bottom:8px}
.follow .sq{width:24px;height:24px}
.copyright{position:absolute;left:0;top:2606px;width:1200px;height:53px;background:var(--green);color:var(--white);font-size:12px;text-align:center;line-height:53px;font-family:"Raleway",sans-serif}
</style>
</head>
<body>

<header class="site-header">
  <div class="brand">
    <div class="brand-mark"></div>
    <div>
      <div class="brand-name">Velmorin</div>
      <div class="brand-tag">Window Treatment Solutions</div>
    </div>
  </div>
  <div class="contact-bar">
    <span class="phone">
      <svg width="20" height="20" viewBox="0 0 20 20"><circle cx="10" cy="10" r="9" fill="none" stroke="#6cbf3c" stroke-width="1.5"/><path d="M6.5 5.5l2 0 1 2.5-1.3 1a6 6 0 0 0 3 3l1-1.3 2.5 1v2c-5 .5-8.7-3.2-8.2-8.2z" fill="#6cbf3c"/></svg>
      555 014 7290
    </span>
    <span class="social-dot"></span>
    <span class="social-dot"></span>
    <span class="social-dot"></span>
  </div>
  <nav class="main-nav">
    <a class="active" href="#">Home</a>
    <a href="#">About Us</a>
    <a href="#">Our Services</a>
    <a href="#">Our Products</a>
    <a href="#">Our Benefits</a>
    <a href="#">Our Gallery</a>
    <a href="#">Contact Us</a>
  </nav>
</header>

<section class="hero">
  <div class="hero-photo" role="img" aria-label="Craftsman in a workshop measuring and marking a wooden board"></div>
  <div class="hero-copy">
    <div class="hero-kicker">We are an international</div>
    <h1 class="hero-title">Window Treatment<span>Solutions company</span></h1>
    <p class="hero-lead">Lorem ipsum dolor sit amet, consectetur adipiscing elit. Aenean ultrices porttitor lacinia. Vestibulum congue metus eleifend dui laoreet rhoncus. Proin placerat eros non egestas malesuada.</p>
    <a class="btn-outline" href="#">View Gallery</a>
  </div>
</section>

<section class="about">
  <h2 class="section-title"><span class="icon-ring"></span><span><em>About</em> Us</span></h2>
  <p class="about-lead">At Velmorin we specialize in custom high quality window treatments. Whether it is for a condo, home or entire building, we provide free sampling, free on site consultation and turnkey installation services to Toronto, the entire GTA and northern cottage community.</p>
  <p class="about-note">We bring over 15 years of expertise serving the design, A/V integrator, builder and architect community, delivering personal attention to every project.</p>
  <p class="about-body">Offering industry leading manufacturers such as Dexavo, we provide top-of-the-line motorized and manual products including blinds, drapes, exterior shades, awnings and bug screens. We carry our own economical product line manufactured in the GTA for budget focused or commercial applications.</p>
</section>

<aside class="estimate">
  <h2 class="section-title"><em>Free</em> Estimate</h2>
  <span class="field">First Name</span>
  <span class="field">Last Name</span>
  <span class="field">Email</span>
  <span class="field">Phone Number</span>
  <span class="field tall">Description</span>
  <a class="btn-outline" href="#">Submit Now!</a>
</aside>

<section class="products">
  <h2 class="section-title"><em>Our</em> Products</h2>
  <svg class="arrow" style="left:28px;top:195px" viewBox="0 0 22 40"><path d="M20 2L3 20l17 18" fill="none" stroke="#333" stroke-width="2"/></svg>
  <svg class="arrow" style="left:1150px;top:195px" viewBox="0 0 22 40"><path d="M2 2l17 18L2 38" fill="none" stroke="#333" stroke-width="2"/></svg>
  <article class="product-card" style="left:80px">
    <div class="product-photo" role="img" aria-label="Covered patio with motorized bug screens" style="background:
      radial-gradient(ellipse 90px 60px at 160px 90px,rgba(235,238,240,.95),rgba(235,238,240,0)),
      radial-gradient(ellipse 120px 40px at 120px 160px,rgba(150,120,90,.9),rgba(150,120,90,0)),
      linear-gradient(180deg,#7a2e22 0%,#8a4a36 14%,#cfd4d6 30%,#9aa49c 60%,#6a5a48 100%)"></div>
    <h3 class="product-name">Motorized Bug Screen</h3>
    <p class="product-desc">Aliquam et magna molestie, dictum tinva magna a, feugiat ante. Aliquam acounts pulvinar purus.</p>
  </article>
  <article class="product-card" style="left:346px">
    <div class="product-photo" role="img" aria-label="Outdoor pavilion with shades overlooking the sea" style="background:
      radial-gradient(ellipse 130px 30px at 120px 30px,rgba(240,238,230,.95),rgba(240,238,230,0)),
      radial-gradient(ellipse 110px 25px at 120px 135px,rgba(140,110,90,.85),rgba(140,110,90,0)),
      linear-gradient(180deg,#3d86cf 0%,#79b3e3 40%,#d7e6f0 58%,#4f8aa0 68%,#d8c9b0 80%,#c2ad8e 100%)"></div>
    <h3 class="product-name">Pavilion Shades</h3>
    <p class="product-desc">Aliquam et magna molestie, dictum tinva magna a, feugiat ante. Aliquam acounts pulvinar purus.</p>
  </article>
  <article class="product-card" style="left:613px">
    <div class="product-photo" role="img" aria-label="Living room with motorized shades and yellow sofa" style="background:
      radial-gradient(ellipse 90px 30px at 140px 140px,rgba(232,190,40,.95),rgba(232,190,40,0)),
      radial-gradient(ellipse 120px 50px at 120px 75px,rgba(200,210,220,.85),rgba(200,210,220,0)),
      linear-gradient(180deg,#5a4236 0%,#b8977a 22%,#cfc8bc 50%,#8a6e58 78%,#4a3a32 100%)"></div>
    <h3 class="product-name">Motorized Shades</h3>
    <p class="product-desc">Aliquam et magna molestie, dictum tinva magna a, feugiat ante. Aliquam acounts pulvinar purus.</p>
  </article>
  <article class="product-card" style="left:879px">
    <div class="product-photo" role="img" aria-label="Lounge with custom drapery and wooden floor" style="background:
      radial-gradient(ellipse 60px 80px at 180px 80px,rgba(70,60,58,.9),rgba(70,60,58,0)),
      radial-gradient(ellipse 80px 70px at 60px 70px,rgba(230,222,206,.9),rgba(230,222,206,0)),
      linear-gradient(180deg,#d9cfbe 0%,#b59a7c 40%,#8e6440 70%,#a8733f 100%)"></div>
    <h3 class="product-name">Custom Drapery</h3>
    <p class="product-desc">Aliquam et magna molestie, dictum tinva magna a, feugiat ante. Aliquam acounts pulvinar purus.</p>
  </article>
</section>

<section class="reviews">
  <h2 class="section-title"><em>Customer</em> Review</h2>
  <svg class="arrow" style="left:28px;top:1859px" viewBox="0 0 22 40"><path d="M20 2L3 20l17 18" fill="none" stroke="#333" stroke-width="2"/></svg>
  <svg class="arrow" style="left:1150px;top:1859px" viewBox="0 0 22 40"><path d="M2 2l17 18L2 38" fill="none" stroke="#333" stroke-width="2"/></svg>
  <div class="review" style="left:80px">
    <div class="avatar" role="img" aria-label="Portrait of customer Mara Ellison"></div>
    <div class="review-body">
      <p class="review-quote"><span class="qmark">“</span> I was reluctant to try coaching, but now I can't imagine life without it. <span class="qmark">”</span></p>
      <p class="review-name">- Mara Ellison</p>
    </div>
  </div>
  <div class="review" style="left:633px">
    <div class="avatar" role="img" aria-label="Portrait of customer Tobin Reyes"></div>
    <div class="review-body">
      <p class="review-quote"><span class="qmark">“</span> Coaching changed my life is ways that I could have never expected! <span class="qmark">”</span></p>
      <p class="review-name">- Tobin Reyes</p>
    </div>
  </div>
</section>

<section class="partners">
  <h2 class="section-title"><em>Our</em> Partners</h2>
  <div class="partner" style="left:80px" role="img" aria-label="Dexavo partner badge"><svg width="196" height="28"><rect width="196" height="28" rx="3" fill="#1e1e1e"/></svg></div>
  <div class="partner" style="left:346px" role="img" aria-label="Quarnel partner badge"><svg width="196" height="54"><rect width="196" height="54" fill="#1d6fb3"/></svg></div>
  <div class="partner" style="left:613px" role="img" aria-label="Harnwick partner badge"><svg width="186" height="62"><rect width="186" height="62" fill="#5d6064"/></svg></div>
  <div class="partner" style="left:879px" role="img" aria-label="Tolvaro authorized dealer badge"><svg width="182" height="78"><rect width="182" height="78" fill="#1f3f8a"/></svg></div>
</section>

<footer class="site-footer">
  <div class="footer-col quick" style="left:80px;width:170px">
    <h3>Quick Links</h3>
    <ul>
      <li>Home</li><li>About Us</li><li>Our Services</li><li>Our Products</li><li>Our Benefits</li><li>Our Gallery</li><li>Contact Us</li>
    </ul>
  </div>
  <div class="footer-col contact" style="left:303px;width:283px">
    <h3>Contact Information</h3>
    <ul>
      <li><svg width="10" height="14" viewBox="0 0 10 14"><path d="M5 0a5 5 0 0 1 5 5c0 4-5 9-5 9S0 9 0 5a5 5 0 0 1 5-5z" fill="#ddd"/><circle cx="5" cy="5" r="2" fill="#23282f"/></svg><span>Lorem ipsum dolor sit amet<br>1240 318 5067<br>PO Box 1480 Ashford DC 6620</span></li>
      <li><svg width="10" height="16" viewBox="0 0 10 16"><path d="M3 1l3 0 0 3-2 1a7 7 0 0 0 0 6l2 1 0 3-3 0C0 12 0 4 3 1z" fill="#ddd"/></svg><span class="call">Freecall 555 014 7290</span></li>
      <li><svg width="14" height="12" viewBox="0 0 14 12"><rect x="0" y="2" width="14" height="9" fill="#ddd"/><path d="M0 2l7 5 7-5" fill="none" stroke="#23282f"/></svg><span>info@velmorin.ca</span></li>
    </ul>
  </div>
  <div class="footer-col newsletter" style="left:640px;width:242px">
    <h3>Newsletter Signup</h3>
    <p>Please enter your email address below to receive our FREE newsletter</p>
    <div class="input">Your Email ID</div>
    <span class="subscribe">Subscribe</span>
  </div>
  <div class="footer-col follow" style="left:934px;width:186px">
    <h3>Follow Us</h3>
    <ul>
      <li><span class="sq" style="background:#3b66a8"></span>Friendloop</li>
      <li><span class="sq" style="background:#d9a21c"></span>Workcircle</li>
      <li><span class="sq" style="background:#3aa0d8"></span>Chirpline</li>
      <li><span class="sq" style="background:#3aa6a0"></span>Email</li>
    </ul>
  </div>
</footer>
<div class="copyright">Copyright 2016@velmorin.ca. All Rights Are Reserved.</div>

</body>
</html>
```